Regenerative Wellness Flyer to recruit Dr offices and clinics

This is a flyer that will be used to recruit new Dr offices and clinics to make them aware of a brand new product that is about to hit the market.

I uploaded an older flyer that I do like. This product is not Stem Cells but fixes a lot of the same things. So the title could be Regenerative Wellness and Cell Factor Therapy.

I also loaded a multiple page info on the product.

I would like to be able to change out logo's & contact information as I have a couple sales people helping push this. I also attached my logo, Velmora. Would like to be able to a QR code...

This is the landing page that the flyer will drive Dr's to:
https://app.pagebrixel.com/v2/preview/K3QwzRtuNaLmBv8Hp2Dx?notrack=true

Target Market(s)

Dr's office, clinics, alternative wellness clinics

Industry/Entity Type

health & wellness

Colors
0054AA
0677BA
7BADD7
CADEEF
E8F1F8
00AB8E
00BBA5
67D7C9
C6EFE9
E9F9F6

Requirements
Nice to have
• The ability to change out the logo/contact info areas

```html
<!DOCTYPE html>
<html lang="en">
<head>
<meta charset="utf-8">
<title>Velmora Wellness – Regenerative Wellness &amp; Cell Factor Therapy</title>
<link href="https://fonts.googleapis.com/css2?family=Montserrat:wght@400;500;600;800&display=swap" rel="stylesheet">
<style>
  :root {
    --blue-deep: #0054AA;
    --blue: #0677BA;
    --blue-soft: #7BADD7;
    --blue-pale: #CADEEF;
    --blue-mist: #E8F1F8;
    --teal: #00AB8E;
    --teal-bright: #00BBA5;
    --teal-soft: #67D7C9;
    --teal-pale: #C6EFE9;
    --teal-mist: #E9F9F6;
    --ink: #1c2733;
    --rule: #9aaab8;
    --paper: #ffffff;
  }
  * { margin: 0; padding: 0; box-sizing: border-box; }
  html, body { width: 848px; height: 1200px; overflow: hidden; background: var(--paper); }
  body { font-family: "Montserrat", Arial, sans-serif; color: var(--ink); }
  .flyer { position: relative; width: 848px; height: 1200px; overflow: hidden; background: var(--paper); }
  .decor { position: absolute; inset: 0; width: 848px; height: 1200px; }

  .brand { position: absolute; left: 58px; top: 44px; width: 134px; text-align: center; }
  .brand-disc { width: 132px; height: 132px; border-radius: 50%; background: var(--blue-pale); margin: 0 auto; }
  .brand-name { margin-top: 12px; font-weight: 800; font-size: 14px; color: var(--blue-deep); white-space: nowrap; }

  .headline { position: absolute; left: 36px; top: 268px; font-weight: 800; font-size: 33px; line-height: 45px; color: var(--blue-deep); letter-spacing: 0.5px; }

  .section-title { position: absolute; left: 32px; font-weight: 600; font-size: 25px; line-height: 34px; color: var(--ink); letter-spacing: 0.3px; }
  .section-bar { position: absolute; left: 32px; width: 160px; height: 3px; background: var(--teal); }
  .section-body { position: absolute; left: 32px; width: 480px; font-size: 15px; line-height: 24.5px; color: var(--ink); }

  .conditions { position: absolute; left: 32px; top: 592px; display: grid; grid-template-columns: 227px 227px; row-gap: 7.3px; list-style: none; font-size: 15.3px; line-height: 24px; }
  .conditions li { position: relative; padding-left: 17px; }
  .conditions li::before { content: ""; position: absolute; left: 2px; top: 9px; width: 6px; height: 6px; border-radius: 50%; background: var(--teal); }

  .divider { position: absolute; left: 523px; top: 575px; width: 1px; height: 600px; background: var(--rule); }

  .callout { position: absolute; left: 530px; top: 640px; width: 304px; text-align: center; font-weight: 500; font-size: 14px; line-height: 23px; letter-spacing: 0.3px; color: var(--blue-deep); }

  .contact { position: absolute; left: 548px; top: 760px; width: 268px; text-align: center; }
  .qr-slot { width: 150px; height: 150px; margin: 0 auto; border: 3px solid var(--blue); border-radius: 8px; background: var(--blue-mist); }
  .qr-caption { margin-top: 12px; font-weight: 600; font-size: 13px; letter-spacing: 1px; color: var(--teal); }
  .contact-rule { width: 60px; height: 3px; background: var(--teal); margin: 22px auto 18px; }
  .rep-name { font-weight: 600; font-size: 17px; color: var(--ink); }
  .rep-role { margin-top: 2px; font-size: 13px; color: var(--blue); }
  .contact-lines { margin-top: 14px; list-style: none; font-size: 13.5px; line-height: 24px; color: var(--ink); }
  .contact-url { margin-top: 10px; font-size: 10.5px; line-height: 15px; color: var(--blue-deep); word-break: break-all; }
</style>
</head>
<body>
<main class="flyer">
  <svg class="decor" viewBox="0 0 1000 1415">
    <defs>
      <clipPath id="photo-window"><circle cx="705" cy="300" r="288"/></clipPath>
      <linearGradient id="photo-tone" x1="0" y1="0" x2="1" y2="1">
        <stop offset="0" stop-color="#eef1f2"/>
        <stop offset="0.55" stop-color="#d8cabd"/>
        <stop offset="1" stop-color="#9fb3c7"/>
      </linearGradient>
    </defs>
    <line x1="350" y1="205" x2="570" y2="-20" stroke="var(--blue-deep)" stroke-width="100" stroke-linecap="round"/>
    <line x1="945" y1="630" x2="1060" y2="515" stroke="var(--teal)" stroke-width="80" stroke-linecap="round"/>
    <circle cx="695" cy="320" r="318" fill="var(--teal-pale)"/>
    <g clip-path="url(#photo-window)">
      <rect x="380" y="0" width="640" height="620" fill="url(#photo-tone)" role="img" aria-label="Photo of a cheerful family of three cheering with raised arms on a beige sofa in a bright living room"/>
    </g>
    <circle cx="0" cy="545" r="18" fill="var(--blue)"/>
    <circle cx="347" cy="520" r="8" fill="none" stroke="var(--teal-soft)" stroke-width="2"/>
    <circle cx="693" cy="643" r="16" fill="none" stroke="var(--blue)" stroke-width="2"/>
    <circle cx="725" cy="620" r="8.5" fill="none" stroke="var(--teal)" stroke-width="2"/>
    <circle cx="857" cy="685" r="9" fill="var(--teal)"/>
    <path d="M240 208h14M247 201v14" stroke="var(--teal-soft)" stroke-width="8" stroke-linecap="round"/>
  </svg>

  <div class="brand">
    <div class="brand-disc"></div>
    <p class="brand-name">Velmora Wellness</p>
  </div>

  <h1 class="headline">REGENERATIVE<br>WELLNESS &amp;<br>CELL FACTOR<br>THERAPY</h1>

  <h2 class="section-title" style="top:498px;">CONDITIONS CELL FACTOR<br>THERAPY MAY HELP</h2>
  <div class="section-bar" style="top:572px;"></div>
  <ul class="conditions">
    <li>Knee Injuries</li><li>Arthritis/Osteoarthritis</li>
    <li>Hip &amp; Labral Tears</li><li>Shoulder Damage</li>
    <li>Chronic Back Pain</li><li>Low Back Pain</li>
    <li>Wrist or Elbow</li><li>Achilles Tendon</li>
    <li>Ankle &amp; Foot Pain</li><li>Plantar Fasciitis</li>
  </ul>

  <h2 class="section-title" style="top:763px;">REGENERATE &amp; REPAIR TISSUE</h2>
  <div class="section-bar" style="top:804px;"></div>
  <p class="section-body" style="top:822px;">Cell factors signal the body's natural internal repair system.<br>They seek out damage and help regenerate the<br>damaged tissue.</p>

  <h2 class="section-title" style="top:907px;">DECREASE PAIN &amp; SORENESS</h2>
  <div class="section-bar" style="top:950px;"></div>
  <p class="section-body" style="top:968px;width:490px;">Cell factors have powerful anti-inflammatory action. Reduced<br>inflammation leads to a decrease in pain &amp;<br>soreness in your body.</p>

  <h2 class="section-title" style="top:1056px;">IMPROVE YOUR HEALTH</h2>
  <div class="section-bar" style="top:1096px;"></div>
  <p class="section-body" style="top:1111px;">Research shows cell factors may benefit a wide variety<br>of health complications and assist you in<br>living a stronger and healthier life.</p>

  <div class="divider"></div>
  <p class="callout">CAPTURE THIS NEW OPPORTUNITY<br>IN YOUR AREA BEFORE ANY<br>OTHER CLINIC</p>

  <section class="contact">
    <div class="qr-slot" role="img" aria-label="QR code linking to the Velmora Wellness clinic landing page"></div>
    <p class="qr-caption">SCAN TO LEARN MORE</p>
    <div class="contact-rule"></div>
    <p class="rep-name">Jordan Ellis</p>
    <p class="rep-role">Clinic Partnerships</p>
    <ul class="contact-lines">
      <li>(555) 014-2290</li>
      <li>jordan@velmorawellness.com</li>
    </ul>
    <p class="contact-url">https://app.pagebrixel.com/v2/preview/K3QwzRtuNaLmBv8Hp2Dx?notrack=true</p>
  </section>
</main>
</body>
</html>
```